Business Card Design

We need a business card for a new furniture company in Utah. We are introducing a fresh new concept in Utah and would like a card to reflect to buyers that they can buy quality furniture and get it NOW. I am open to just about any color scheme, but I would like something that pops.

Business

Sofa Harbor, Lenn Varcoe
41 S. East Pine Lane
Cedar Hollow Utah 84117

```html
<!DOCTYPE html>
<html lang="en">
<head>
<meta charset="utf-8">
<title>Sofa Harbor – Business Card</title>
<link rel="stylesheet" href="https://fonts.googleapis.com/css2?family=Tinos&display=swap">
<style>
  :root {
    --page-bg: #2b1a1a;
    --card-edge: #1f140d;
    --silver-light: #f4f4f4;
    --silver-mid: #a9b1b6;
    --silver-dark: #6c767c;
    --card-brown: #3b2517;
    --card-brown-deep: #2c1a10;
    --gold: #c9993d;
    --brand-silver: #dcdcdc;
    --contact-text: #ece6de;
  }
  * { margin: 0; padding: 0; box-sizing: border-box; }
  html, body {
    width: 1200px;
    height: 800px;
    overflow: hidden;
    background: var(--page-bg);
    font-family: "Tinos", "Times New Roman", serif;
  }
  .card {
    position: absolute;
    left: 100px;
    top: 110px;
    width: 1000px;
    height: 580px;
    background: var(--card-edge);
    padding: 8px;
  }
  .card__frame {
    width: 100%;
    height: 100%;
    padding: 12px;
    background: linear-gradient(135deg, var(--silver-dark) 0%, var(--silver-light) 30%, var(--silver-mid) 55%, var(--silver-light) 80%, var(--silver-dark) 100%);
  }
  .card__face {
    position: relative;
    width: 100%;
    height: 100%;
    background: linear-gradient(160deg, var(--card-brown) 0%, var(--card-brown-deep) 100%);
  }
  .brand {
    position: absolute;
    left: 56px;
    top: 60px;
    display: flex;
    align-items: center;
    gap: 28px;
  }
  .brand__mark {
    width: 96px;
    height: 96px;
    background: var(--gold);
  }
  .brand__name {
    font-size: 66px;
    color: var(--brand-silver);
    letter-spacing: 2px;
  }
  .person {
    position: absolute;
    left: 56px;
    top: 272px;
    font-size: 36px;
    color: var(--gold);
  }
  .contacts {
    position: absolute;
    left: 56px;
    top: 330px;
    list-style: none;
    font-size: 28px;
    line-height: 36px;
    color: var(--contact-text);
  }
  .contacts__item {
    display: flex;
    align-items: center;
    gap: 12px;
  }
  .contacts__icon {
    width: 24px;
    height: 24px;
    flex: none;
  }
  .contacts__item--plain { padding-left: 36px; }
</style>
</head>
<body>
  <div class="card">
    <div class="card__frame">
      <div class="card__face">
        <div class="brand">
          <div class="brand__mark"></div>
          <div class="brand__name">Sofa Harbor</div>
        </div>
        <div class="person">Lenn Varcoe</div>
        <ul class="contacts">
          <li class="contacts__item">
            <svg class="contacts__icon" viewBox="0 0 24 24"><path fill="#c9993d" d="M6.6 10.8a15 15 0 0 0 6.6 6.6l2.2-2.2a1 1 0 0 1 1-.25 11.4 11.4 0 0 0 3.6.57 1 1 0 0 1 1 1V20a1 1 0 0 1-1 1A17 17 0 0 1 3 4a1 1 0 0 1 1-1h3.5a1 1 0 0 1 1 1c0 1.25.2 2.45.57 3.57a1 1 0 0 1-.25 1z"/></svg>
            <span>1586 472 903</span>
          </li>
          <li class="contacts__item">
            <svg class="contacts__icon" viewBox="0 0 24 24" fill="none" stroke="#c9993d" stroke-width="1.8"><circle cx="12" cy="12" r="9.5"/><ellipse cx="12" cy="12" rx="4" ry="9.5"/><path d="M2.5 12h19M4 7h16M4 17h16"/></svg>
            <span>www.sofaharbor.com</span>
          </li>
          <li class="contacts__item">
            <svg class="contacts__icon" viewBox="0 0 24 24"><rect x="2" y="5" width="20" height="14" fill="#c9993d"/><path d="M2 5l10 8 10-8" fill="none" stroke="#2c1a10" stroke-width="1.6"/></svg>
            <span>info@sofaharbor.com</span>
          </li>
          <li class="contacts__item">
            <svg class="contacts__icon" viewBox="0 0 24 24"><path fill="#c9993d" d="M12 3l10 9h-3v9h-5v-6h-4v6H5v-9H2z"/></svg>
            <span>41 S. East Pine Lane</span>
          </li>
          <li class="contacts__item contacts__item--plain">Cedar Hollow Utah 84117</li>
        </ul>
      </div>
    </div>
  </div>
</body>
</html>
```